Business Card Design

We need a business card designed for our new company. Prefer a black card with white logo & writing.

Contact Information for Business Card

Dale Pickett, address: 7-4417 Larchmere Avenue, Fernvale, BC, V3K 2R9, Office Phone: 604-555-0172, Cell: 604-555-0138, Email: dale@kelsoncoatworks.ca

Colors

Designer to choose only greyscale colors for use in the design.

```html
<!DOCTYPE html>
<html lang="en">
<head>
<meta charset="utf-8">
<title>Kelson Coatworks – Business Card</title>
<link href="https://fonts.googleapis.com/css2?family=Arimo:wght@400;700&display=swap" rel="stylesheet">
<style>
  :root {
    --backdrop: #b3b3b3;
    --card-dark: #353535;
    --card-white: #fbfbfb;
    --band-light: #9b9b9b;
    --band-dark: #484b4f;
    --stripe-dark: #3a3a3a;
    --stripe-light: #e9e9e9;
    --chip-grey: #8e8e8e;
    --name-chip: #6f6f6f;
    --ink-white: #ffffff;
    --ink-black: #1f1f1f;
  }
  * { margin: 0; padding: 0; box-sizing: border-box; }
  html, body { width: 1200px; height: 900px; overflow: hidden; }
  body {
    background: var(--backdrop);
    font-family: "Arimo", Arial, sans-serif;
    position: relative;
  }
  .card {
    position: absolute;
    top: 320px;
    width: 424px;
    height: 256px;
    background: var(--card-dark);
    overflow: hidden;
  }
  .card--front { left: 139px; }
  .card--back { left: 664px; }
  .card__shapes { position: absolute; inset: 0; width: 424px; height: 256px; }

  .wordmark {
    position: absolute;
    transform: translate(-50%, -50%);
    text-align: center;
    font-weight: 700;
    line-height: 1.05;
    letter-spacing: 1px;
  }
  .wordmark__line--main { font-size: 30px; }
  .wordmark__line--sub { font-size: 15px; letter-spacing: 5px; margin-top: 4px; }
  .wordmark--light { color: var(--ink-white); left: 212px; top: 109px; }
  .wordmark--dark { color: var(--ink-black); left: 327px; top: 111px; }
  .wordmark--dark .wordmark__line--main { font-size: 24px; }
  .wordmark--dark .wordmark__line--sub { font-size: 12px; }

  .tagline {
    position: absolute;
    top: 215px;
    height: 14px;
    padding: 0 2px;
    background: var(--stripe-dark);
    color: var(--ink-white);
    font-size: 9.5px;
    line-height: 14px;
    white-space: nowrap;
  }
  .card--front .tagline { left: 48px; }
  .card--back .tagline { left: 39px; }

  .web-address {
    position: absolute;
    top: 216px;
    height: 13px;
    color: var(--ink-white);
    font-size: 9px;
    line-height: 13px;
    letter-spacing: 2.1px;
    white-space: nowrap;
  }
  .web-address__chip { background: var(--chip-grey); padding: 0 1px; }
  .card--front .web-address { left: 250px; }
  .card--back .web-address { left: 249px; }

  .person-name {
    position: absolute;
    left: 31px;
    top: 38px;
    font-size: 17px;
    color: var(--ink-white);
    white-space: nowrap;
  }
  .person-name__first { font-weight: 700; }
  .person-name__last { background: var(--name-chip); padding: 0 3px; font-weight: 400; }

  .contact-list { position: absolute; left: 31px; top: 0; list-style: none; }
  .contact-item { position: absolute; left: 0; width: 260px; }
  .contact-item__icon { position: absolute; left: 0; width: 11px; height: 11px; }
  .contact-item__text {
    position: absolute;
    left: 20px;
    color: var(--ink-white);
    font-size: 9.5px;
    line-height: 11.5px;
    white-space: nowrap;
  }
  .contact-item--phone { top: 109px; }
  .contact-item--phone .contact-item__icon { top: 7px; }
  .contact-item--email { top: 140px; }
  .contact-item--email .contact-item__icon { top: 1px; }
  .contact-item--address { top: 159px; }
  .contact-item--address .contact-item__icon { top: 10px; }
  .contact-item--address .contact-item__text { line-height: 16px; }
</style>
</head>
<body>

  <section class="card card--front" aria-label="Business card front">
    <svg class="card__shapes" viewBox="0 0 424 256" aria-hidden="true">
      <polygon points="0,203 217,203 209,240 0,240" fill="var(--band-light)"/>
      <polygon points="221,203 424,203 424,240 214,240" fill="var(--band-dark)"/>
      <g fill="var(--stripe-dark)">
        <polygon points="10,203 17,203 23,210 16,210"/>
        <polygon points="21,203 28,203 34,210 27,210"/>
        <polygon points="32,203 39,203 45,210 38,210"/>
        <polygon points="43,203 50,203 56,210 49,210"/>
      </g>
      <g fill="var(--card-dark)">
        <polygon points="369,203 376,203 370,210 363,210"/>
        <polygon points="380,203 387,203 381,210 374,210"/>
        <polygon points="391,203 398,203 392,210 385,210"/>
        <polygon points="402,203 409,203 403,210 396,210"/>
      </g>
    </svg>

    <div class="wordmark wordmark--light">
      <div class="wordmark__line--main">KELSON</div>
      <div class="wordmark__line--sub">COATWORKS</div>
    </div>

    <p class="tagline">YOUR EPOXY SOLUTION</p>
    <p class="web-address"><span class="web-address__chip">www.</span>kelsoncoatworks<span class="web-address__chip">.shop</span></p>
  </section>

  <section class="card card--back" aria-label="Business card back">
    <svg class="card__shapes" viewBox="0 0 424 256" aria-hidden="true">
      <polygon points="252,0 424,0 424,256 186,256" fill="var(--card-white)"/>
      <polygon points="0,203 216,203 208,240 0,240" fill="var(--band-light)"/>
      <polygon points="222,203 424,203 424,240 213,240" fill="var(--band-dark)"/>
      <g fill="var(--stripe-dark)">
        <polygon points="9,203 16,203 22,210 15,210"/>
        <polygon points="20,203 27,203 33,210 26,210"/>
        <polygon points="31,203 38,203 44,210 37,210"/>
        <polygon points="42,203 49,203 55,210 48,210"/>
      </g>
      <g fill="var(--stripe-light)">
        <polygon points="368,203 375,203 369,210 362,210"/>
        <polygon points="379,203 386,203 380,210 373,210"/>
        <polygon points="390,203 397,203 391,210 384,210"/>
        <polygon points="401,203 408,203 402,210 395,210"/>
      </g>
    </svg>

    <h1 class="person-name"><span class="person-name__first">DALE</span> <span class="person-name__last">PICKETT</span></h1>

    <ul class="contact-list">
      <li class="contact-item contact-item--phone">
        <svg class="contact-item__icon" viewBox="0 0 11 11" aria-hidden="true">
          <rect width="11" height="11" fill="var(--chip-grey)"/>
          <path d="M3.2 2.6c.4-.3.8-.2 1 .2l.5 1c.1.3 0 .5-.2.7l-.3.3c.3.7.9 1.3 1.6 1.6l.3-.3c.2-.2.5-.3.7-.2l1 .5c.4.2.5.6.2 1l-.4.4c-.4.4-1 .4-1.6.1C4.7 7.2 3.8 6.3 3.1 5 2.8 4.4 2.8 3.8 3.2 3.4z" fill="var(--ink-white)"/>
        </svg>
        <span class="contact-item__text">604-555-0172 (Office)<br>604-555-0138 (Cell)</span>
      </li>
      <li class="contact-item contact-item--email">
        <svg class="contact-item__icon" viewBox="0 0 11 11" aria-hidden="true">
          <rect width="11" height="11" fill="var(--chip-grey)"/>
          <rect x="2.5" y="3.3" width="6" height="4.4" fill="var(--ink-white)"/>
          <path d="M2.5 3.3 5.5 5.8 8.5 3.3" fill="none" stroke="var(--chip-grey)" stroke-width=".7"/>
        </svg>
        <span class="contact-item__text">dale@kelsoncoatworks.ca</span>
      </li>
      <li class="contact-item contact-item--address">
        <svg class="contact-item__icon" viewBox="0 0 11 11" aria-hidden="true">
          <rect width="11" height="11" fill="var(--chip-grey)"/>
          <path d="M5.5 2.2a2.3 2.3 0 0 1 2.3 2.3c0 1.7-2.3 4.3-2.3 4.3S3.2 6.2 3.2 4.5a2.3 2.3 0 0 1 2.3-2.3z" fill="var(--ink-white)"/>
          <circle cx="5.5" cy="4.5" r=".8" fill="var(--chip-grey)"/>
        </svg>
        <span class="contact-item__text">7-4417 Larchmere Avenue,<br>Fernvale, BC, V3K 2R9</span>
      </li>
    </ul>

    <div class="wordmark wordmark--dark">
      <div class="wordmark__line--main">KELSON</div>
      <div class="wordmark__line--sub">COATWORKS</div>
    </div>

    <p class="tagline">An E-commerce Website</p>
    <p class="web-address"><span class="web-address__chip">www.</span>kelsoncoatworks<span class="web-address__chip">.shop</span></p>
  </section>

</body>
</html>
```